Tolvern landscape website

Our company is called Tolvern Landscape, Inc. We are located in Oak Bluffs, Martha's Vineyard Island, MA. We are a design construction maintenance firm offering a wide variety of services. We need to build a website for our Landscape, Construction, and Maintenance Company. The ability to interchange photos in many locations. 6-7 Tabs for individualized services. Ability to change and alter text. Use of our logo to increase branding. Modern, clean, simplified backgrounds are appealing. Possibly black background to allow the colors of flowers and logos to pop. Simplicity in management is of importance! The final design should lend itself to an upscale marketplace.
Updates

Dear Designers, Please be advised that the web design needs coding as well. Coding will not be charged on top of whatever investment and must be inclusive in the package. In short, you will not ask the client for more funds. -BriefHarbor Admin (Tomas Aldrete)

Target Market(s)

These are second homeowners. estate type properties. upscale clientele.

Industry/Entity Type

Construction

Requirements
Must have
• multiple tabs 6-7 to be able to highlight services. space for text and photos/albums. easy to navigate.
Should not have
• cheesy gimmicky cheap type feel

```html
<!DOCTYPE html>
<html lang="en">
<head>
<meta charset="utf-8">
<title>Tolvern Landscape Construction</title>
<link rel="stylesheet" href="https://fonts.googleapis.com/css2?family=Arimo:wght@400;700&family=Tinos:wght@400;700&display=swap">
<style>
  :root {
    --bar: #060606;
    --nav-active: #3b3b3b;
    --nav-text: #d8d8d8;
    --sky-top: #2f86c6;
    --sky-mid: #62a9dc;
    --sky-light: #cfe2f0;
    --panel: rgba(22, 48, 68, 0.92);
    --gold: #f2b01e;
    --rule-gold: #c79a3a;
    --features-bg: #2a2a2a;
    --features-rule: #3c3c3c;
    --circle: #3a3a3a;
    --icon: #9a9a9a;
    --title: #d6d6d6;
    --muted: #7b7b7b;
    --heading-grey: #7d7d7d;
    --works-bg: #0e0e0e;
    --caption: #bdbdbd;
    --body-light: #cfcfcf;
    --footer-bg: #050505;
    --white: #ffffff;
  }
  * { box-sizing: border-box; margin: 0; padding: 0; }
  html, body { width: 1200px; height: 1058px; overflow: hidden; background: var(--bar); }
  body { font-family: "Arimo", Arial, sans-serif; position: relative; }
  .page { position: relative; width: 1200px; height: 1058px; overflow: hidden; }

  /* top bar */
  .topbar { position: absolute; left: 0; top: 0; width: 1200px; height: 44px; background: var(--bar); z-index: 3; }
  .brand { position: absolute; left: 270px; top: 0; width: 225px; height: 83px; background: var(--white); z-index: 4;
           display: flex; align-items: center; gap: 12px; padding-left: 14px; }
  .brand-dot { width: 62px; height: 62px; border-radius: 50%; background: #2f6b3a; flex: none; }
  .brand-name { font-family: "Tinos", "Times New Roman", serif; color: #2a2a2a; }
  .brand-name strong { display: block; font-weight: 400; font-size: 25px; letter-spacing: 0.5px; line-height: 1; }
  .brand-name span { display: block; font-size: 9px; font-weight: 400; letter-spacing: 0.3px; margin-top: 6px; }
  .nav { position: absolute; top: 0; left: 658px; display: flex; height: 44px; }
  .nav a { color: var(--nav-text); text-decoration: none; font-size: 9px; height: 44px; line-height: 44px; padding: 0 13px; }
  .nav a.is-active { background: var(--nav-active); color: var(--white); padding: 0 10px; }

  /* hero */
  .hero { position: absolute; left: 0; top: 44px; width: 1200px; height: 314px;
          background: linear-gradient(100deg, var(--sky-top) 0%, var(--sky-mid) 40%, var(--sky-light) 62%, #8fbde0 78%, #1a1a1a 96%); }
  .hero-panel { position: absolute; left: 270px; top: 109px; width: 223px; height: 194px; background: var(--panel); z-index: 2; padding: 0 33px 0 32px; }
  .hero-phone { display: flex; align-items: center; gap: 8px; color: var(--gold); font-size: 15px; margin-top: 26px; height: 18px; }
  .hero-rule { border-top: 1px solid rgba(255,255,255,0.15); margin-top: 13px; }
  .hero-title { color: var(--white); font-size: 18px; font-weight: 400; line-height: 21px; margin-top: 13px; }
  .hero-arrows { position: absolute; left: 32px; top: 158px; }

  /* features */
  .features { position: absolute; left: 0; top: 358px; width: 1200px; height: 299px; background: var(--features-bg); }
  .features-kicker { position: absolute; top: 40px; width: 100%; text-align: center; color: #a5a5a5; font-size: 11px; }
  .features-title { position: absolute; top: 54px; width: 100%; text-align: center; color: var(--heading-grey); font-size: 17px; font-weight: 400; }
  .features-rule { position: absolute; left: 400px; top: 88px; width: 436px; border-top: 1px solid var(--features-rule); }
  .feature { position: absolute; width: 200px; }
  .feature-icon { position: absolute; left: 0; top: 0; width: 40px; height: 40px; border-radius: 50%; background: var(--circle);
                  display: flex; align-items: center; justify-content: center; }
  .feature-body { position: absolute; left: 49px; top: 4px; width: 150px; }
  .feature-title { color: var(--title); font-size: 11px; font-weight: 400; padding-bottom: 6px; border-bottom: 1px solid var(--features-rule); width: 115px; }
  .feature.is-highlight .feature-title { color: var(--gold); }
  .feature-text { color: var(--muted); font-size: 8px; line-height: 10.5px; margin-top: 5px; }
  .feature.is-highlight .feature-text { color: #a8a8a8; }

  /* works */
  .works { position: absolute; left: 0; top: 657px; width: 1200px; height: 308px;
           background: linear-gradient(160deg, #1d1d1d 0%, #0a0a0a 45%, #141414 100%); }
  .work { position: absolute; top: 40px; width: 206px; }
  .work-photo { width: 206px; height: 140px; }
  .photo-tower { background: linear-gradient(135deg, #dfe9ee 0%, #5fb2c6 45%, #1f5e6e 100%); }
  .photo-phone { background: linear-gradient(135deg, #e7e5df 0%, #a9a9a5 50%, #5b6670 100%); }
  .photo-worker { background: linear-gradient(135deg, #b9b5ae 0%, #8a7c6a 45%, #1f2a3d 100%); }
  .work-caption { color: var(--caption); font-size: 7.5px; text-transform: uppercase; margin-top: 11px; padding-bottom: 9px; border-bottom: 1px solid #3a3a3a; }
  .work-text { color: var(--body-light); font-size: 7.5px; line-height: 10.5px; margin-top: 9px; height: 42px; }
  .work-more { color: #8a8a8a; font-size: 6px; margin-top: 0; display: block; text-decoration: none; }

  /* footer */
  .footer-rule { position: absolute; left: 0; top: 965px; width: 1200px; height: 2px; background: var(--rule-gold); }
  .footer { position: absolute; left: 0; top: 967px; width: 1200px; height: 91px; background: var(--footer-bg); }
  .footer-mark { position: absolute; left: 270px; top: 28px; width: 50px; height: 50px; border-radius: 50%; background: #2e2e2e; }
  .footer-name { position: absolute; left: 340px; top: 28px; color: #cfcfcf; font-size: 11px; }
  .footer-sub { position: absolute; left: 340px; top: 45px; color: #9a9a9a; font-size: 8px; }
  .footer-legal { position: absolute; left: 340px; top: 66px; color: #8a8a8a; font-size: 8px; }
  .footer-divider { position: absolute; left: 482px; top: 22px; height: 52px; border-left: 1px solid #2a2a2a; }
  .social { position: absolute; left: 518px; top: 30px; display: flex; gap: 4px; }
  .social span { width: 15px; height: 15px; background: #2d2d2d; display: block; }
</style>
</head>
<body>
<div class="page">
  <header class="topbar">
    <nav class="nav">
      <a class="is-active" href="#">About Us</a>
      <a href="#">Services</a>
      <a href="#">Portfolio</a>
      <a href="#">Career</a>
      <a href="#">Contact</a>
    </nav>
  </header>
  <div class="brand">
    <span class="brand-dot"></span>
    <div class="brand-name"><strong>TOLVERN</strong><span>LANDSCAPE CONSTRUCTION</span></div>
  </div>

  <section class="hero" role="img" aria-label="Silhouette of a roofer working on a roof against a blue sky with clouds"></section>
  <div class="hero-panel">
    <div class="hero-phone">
      <svg width="10" height="12" viewBox="0 0 10 12"><path d="M2 0.5 L4 3 L3 4.5 Q4 7.5 6 8.5 L7.5 7.5 L9.5 9.5 L8 11.5 Q3 11 0.5 3 Z" fill="var(--gold)"/></svg>
      <span>+1 508 555 0142</span>
    </div>
    <div class="hero-rule"></div>
    <h1 class="hero-title">We are ready to manage projects of any complexity</h1>
    <svg class="hero-arrows" width="20" height="14" viewBox="0 0 20 14"><path d="M7 1 L2 7 L7 13 M13 1 L18 7 L13 13" stroke="#9fb4c4" stroke-width="1.2" fill="none"/></svg>
  </div>

  <section class="features">
    <p class="features-kicker">Welcome to our company website!</p>
    <h2 class="features-title">We are the leaders in the construction industry</h2>
    <div class="features-rule"></div>

    <div class="feature" style="left:270px; top:109px;">
      <div class="feature-icon"><svg width="22" height="22" viewBox="0 0 22 22"><circle cx="8" cy="13" r="5" fill="none" stroke="var(--icon)" stroke-width="3" stroke-dasharray="2 1.5"/><circle cx="15" cy="7" r="3.5" fill="none" stroke="var(--icon)" stroke-width="2.5" stroke-dasharray="1.6 1.2"/></svg></div>
      <div class="feature-body"><h3 class="feature-title">Ut enim ad minim</h3><p class="feature-text">odio dignissimos ducimus qui blanditiis praesentium volupta. tum deleniti atque corrupti.</p></div>
    </div>
    <div class="feature" style="left:499px; top:109px;">
      <div class="feature-icon"><svg width="20" height="18" viewBox="0 0 20 18"><rect x="2" y="1" width="16" height="16" fill="none" stroke="var(--icon)" stroke-width="1.5"/><rect x="5" y="4" width="5" height="4" fill="var(--icon)"/><path d="M11 5h4M11 7.5h4M5 10.5h10M5 13h10" stroke="var(--icon)" stroke-width="1"/></svg></div>
      <div class="feature-body"><h3 class="feature-title">Ut enim ad minim</h3><p class="feature-text">odio dignissimos ducimus qui blanditiis praesentium volupta. tum deleniti atque corrupti.</p></div>
    </div>
    <div class="feature" style="left:730px; top:109px;">
      <div class="feature-icon"><svg width="16" height="18" viewBox="0 0 16 18"><path d="M4 8V5a4 4 0 0 1 8 0v3" fill="none" stroke="var(--icon)" stroke-width="2"/><rect x="2" y="8" width="12" height="9" rx="1" fill="var(--icon)"/><rect x="7.2" y="11" width="1.6" height="3" fill="var(--circle)"/></svg></div>
      <div class="feature-body"><h3 class="feature-title">Ut enim ad minim</h3><p class="feature-text">odio dignissimos ducimus qui blanditiis praesentium volupta. tum deleniti atque corrupti.</p></div>
    </div>

    <div class="feature is-highlight" style="left:270px; top:196px;">
      <div class="feature-icon"><svg width="20" height="20" viewBox="0 0 20 20"><path d="M3 17 L4 13 L14 3 L17 6 L7 16 Z" fill="var(--gold)"/><path d="M3 17 L4 13 L7 16 Z" fill="#f7d57a"/></svg></div>
      <div class="feature-body"><h3 class="feature-title">Ut enim ad minim</h3><p class="feature-text">odio dignissimos ducimus qui blanditiis praesentium volupta. tum deleniti atque corrupti.</p></div>
    </div>
    <div class="feature" style="left:499px; top:196px;">
      <div class="feature-icon"><svg width="14" height="20" viewBox="0 0 14 20"><path d="M7 1a6 6 0 0 0-3.5 10.9V14h7v-2.1A6 6 0 0 0 7 1z" fill="var(--icon)"/><rect x="4" y="15" width="6" height="1.5" fill="var(--icon)"/><rect x="5" y="17.5" width="4" height="1.5" fill="var(--icon)"/></svg></div>
      <div class="feature-body"><h3 class="feature-title">Ut enim ad minim</h3><p class="feature-text">odio dignissimos ducimus qui blanditiis praesentium volupta. tum deleniti atque corrupti.</p></div>
    </div>
    <div class="feature" style="left:730px; top:196px;">
      <div class="feature-icon"><svg width="20" height="20" viewBox="0 0 20 20"><circle cx="10" cy="10" r="8" fill="none" stroke="var(--icon)" stroke-width="2"/><path d="M10 5v5h4" fill="none" stroke="var(--icon)" stroke-width="2"/></svg></div>
      <div class="feature-body"><h3 class="feature-title">Ut enim ad minim</h3><p class="feature-text">odio dignissimos ducimus qui blanditiis praesentium volupta. tum deleniti atque corrupti.</p></div>
    </div>
  </section>

  <section class="works">
    <article class="work" style="left:270px;">
      <div class="work-photo photo-tower" role="img" aria-label="Curved glass office tower seen from below"></div>
      <h3 class="work-caption">Ut enim ad minim veniam quis</h3>
      <p class="work-text">Lorem ipsum dolor sit amet, consectetur adipisicing elit, sed do eiusmod tempor incididunt ut labore et dolore magna aliqua. Ut enim ad minim veniam, quis nostrud exercitation ullamco laboris.</p>
      <a class="work-more" href="#">[ READ MORE ]</a>
    </article>
    <article class="work" style="left:488px;">
      <div class="work-photo photo-phone" role="img" aria-label="Site manager in a hard hat on a phone call with a colleague"></div>
      <h3 class="work-caption">Excepteur sint occaecat</h3>
      <p class="work-text">Lorem ipsum dolor sit amet, consectetur adipisicing elit, sed do eiusmod tempor incididunt ut labore et dolore magna aliqua. Ut enim ad minim veniam</p>
      <a class="work-more" href="#">[ READ MORE ]</a>
    </article>
    <article class="work" style="left:706px;">
      <div class="work-photo photo-worker" role="img" aria-label="Construction worker in a white hard hat at an industrial site"></div>
      <h3 class="work-caption">Temporibus autem quibusdam</h3>
      <p class="work-text">Lorem ipsum dolor sit amet, consectetur adipisicing elit, sed do eiusmod tempor incididunt ut labore et dolore magna aliqua. Ut enim ad minim veniam, quis nostrud</p>
      <a class="work-more" href="#">[ READ MORE ]</a>
    </article>
  </section>

  <div class="footer-rule"></div>
  <footer class="footer">
    <span class="footer-mark"></span>
    <p class="footer-name">Tolvern</p>
    <p class="footer-sub">Landscape Construction</p>
    <p class="footer-legal">© 2014 | PRIVACY POLICY</p>
    <div class="footer-divider"></div>
    <div class="social" aria-label="Social links"><span></span><span></span><span></span><span></span></div>
  </footer>
</div>
</body>
</html>
```